Business card design needed

Our company background is that we provides transfers to and from the airport, social & corporate events, weddings.
We are also available for charter for birthday party, wine tastings, concerts, anniversary, school balls etc.
Our business cards have to reflect that we have a professional company, they are our first contact and have to stand out from the other 'players' in the market.

Industry/Entity Type

School

Contact Information for Business Card

VESTAR PTH, Teodor & Marguerite, mob: 0427 381 592, PO Box 284, Brennick WA 6172, ABN 52 614 203 178, Lic 7169/2058,

Requirements
Must have
• Telephone number: 0427 381 592
Website: www.VESTARPTH.com.au
postal address: PO Box 284, Brennick WA 6172
Licences: Lic 7169/2058

***If using the new photo (one with the bus and buildings behind it), if possible can the buildings be cropped out. Thanks
Nice to have
• would be nice to have the pics of the vehicle(s), preferred the Vel on the card but not too fussed.
Should not have
• Picture of vehicle we don't have in our fleet. (We ONLY have the Velarions and Murako Densa mini bus)

```html
<!DOCTYPE html>
<html lang="en">
<head>
<meta charset="utf-8">
<title>VESTAR PTH – Business Card</title>
<link rel="stylesheet" href="https://fonts.googleapis.com/css2?family=Merriweather:wght@700;900&display=swap">
<style>
  :root {
    --stage: #3a3a3a;
    --card-black: #050505;
    --card-tuft: #1a1a1a;
    --silver-light: #f4f4f4;
    --silver-mid: #cfcfcf;
    --frame-dark: #5a5a5a;
    --ink: #111111;
    --logo-silver: #e6e6e6;
  }
  html, body {
    margin: 0;
    padding: 0;
    width: 1200px;
    height: 900px;
    overflow: hidden;
    background: var(--stage);
  }
  .stage {
    position: relative;
    width: 1200px;
    height: 900px;
    font-family: "Merriweather", Georgia, serif;
  }
  .card {
    position: absolute;
    top: 303px;
    width: 525px;
    height: 294px;
    background: radial-gradient(ellipse at 50% 50%, var(--card-tuft) 0%, var(--card-black) 70%);
    overflow: hidden;
  }
  .card--front { left: 58px; }
  .card--back { left: 617px; }

  .brand-name {
    position: absolute;
    top: 123px;
    width: 240px;
    margin: 0;
    text-align: center;
    white-space: nowrap;
    font-weight: 900;
    font-size: 26px;
    line-height: 44px;
    letter-spacing: 0.5px;
    color: var(--logo-silver);
  }
  .card--front .brand-name { left: 16px; }
  .card--back .brand-name { left: 267px; }

  .vehicle-frame {
    position: absolute;
    left: 273px;
    top: 91px;
    width: 252px;
    height: 112px;
    box-sizing: border-box;
    padding: 8px 0 8px 9px;
    background: linear-gradient(180deg, var(--silver-light), var(--silver-mid));
    border: 2px solid var(--frame-dark);
    border-right: none;
  }
  .vehicle-photo {
    width: 100%;
    height: 100%;
    background: linear-gradient(180deg, #7b7a72 0%, #a8a59a 45%, #6b665e 100%);
  }

  .contact-panel {
    position: absolute;
    left: 0;
    top: 91px;
    width: 250px;
    height: 112px;
    box-sizing: border-box;
    padding: 14px 0 0 22px;
    background: linear-gradient(135deg, var(--silver-light) 0%, #ffffff 40%, var(--silver-mid) 100%);
    border: 3px solid var(--frame-dark);
    border-left: none;
    color: var(--ink);
  }
  .contact-names {
    margin: 0 0 9px;
    font-size: 17px;
    font-weight: 900;
    line-height: 22px;
  }
  .contact-line {
    margin: 0;
    font-size: 11px;
    font-weight: 700;
    line-height: 16px;
    white-space: nowrap;
  }
  .contact-line--mobile { font-size: 13px; line-height: 17px; margin-bottom: 1px; }
</style>
</head>
<body>
  <main class="stage">
    <section class="card card--front" aria-label="Business card front">
      <p class="brand-name">VESTAR PTH</p>
      <div class="vehicle-frame">
        <div class="vehicle-photo" role="img" aria-label="Photo of a silver Velarions sedan parked on a street"></div>
      </div>
    </section>

    <section class="card card--back" aria-label="Business card back">
      <div class="contact-panel">
        <h1 class="contact-names">Teodor &amp; Marguerite</h1>
        <p class="contact-line contact-line--mobile">mob: 0427 381 592</p>
        <p class="contact-line">PO Box 284, Brennick WA 6172,</p>
        <p class="contact-line">ABN 52 614 203 178, Lic 7169/2058</p>
      </div>
      <p class="brand-name">VESTAR PTH</p>
    </section>
  </main>
</body>
</html>
```